Stationery Design Project - Ta fourmilière

We are a french company, Ta Fourmilière. It means Your Anthill.
We own and manage woods, we transform it industrially into very high quality (dry) logs and pellets and we commercialize them to individuals in France.
People can order the logs online or by phone and get the wood logs delivered at home.

After our great logo contest, we would like to launch a new stationery project.

Target Market(s)

inhabitants of sub-urban areas in France. (living in houses not in apartment )

Industry/Entity Type

It Company

Requirements
Must have
• content see attachment
logo

For the business card, we would like on the front side, the logo, name + contact info. We would like to use the back side for commercial purpose insisting on our distinctive value proposition.
Nice to have
• the back side of the business card can be more colorful

```html
<!DOCTYPE html>
<html lang="fr">
<head>
<meta charset="utf-8">
<title>Ta Fourmilière – carte de visite verso</title>
<link rel="stylesheet" href="https://fonts.googleapis.com/css2?family=Arimo:wght@700&display=swap">
<style>
  :root {
    --yellow: #f6c51f;
    --yellow-deep: #e9b410;
    --ink: #1d1b16;
    --band: #111111;
    --figure-red: #b3262a;
    --figure-navy: #1f2f55;
    --figure-boot: #6b4a2b;
  }
  * { margin: 0; padding: 0; box-sizing: border-box; }
  html, body { width: 1200px; height: 741px; overflow: hidden; background: var(--band); }
  .card {
    position: relative;
    width: 1200px;
    height: 741px;
    font-family: "Arimo", Arial, sans-serif;
    font-weight: 700;
    overflow: hidden;
  }
  .card__field {
    position: absolute;
    inset: 0 0 189px 0;
    background: radial-gradient(ellipse at 60% 40%, var(--yellow) 0%, var(--yellow) 55%, var(--yellow-deep) 100%);
  }
  .card__band {
    position: absolute;
    left: 0; right: 0; bottom: 0;
    height: 189px;
    background: var(--band);
  }
  .mascot {
    position: absolute;
    left: 16px;
    top: 32px;
    width: 180px;
    height: 536px;
    border-radius: 60px 60px 20px 20px;
    background: linear-gradient(180deg, var(--figure-red) 0%, var(--figure-red) 45%, var(--figure-navy) 55%, var(--figure-navy) 86%, var(--figure-boot) 100%);
  }
  .pitch {
    position: absolute;
    right: 14px;
    top: 158px;
    text-align: right;
    color: var(--ink);
    font-size: 29px;
    letter-spacing: 1.9px;
    line-height: 40px;
    white-space: nowrap;
  }
  .pitch__gap { display: block; height: 40px; }
  .signature {
    position: absolute;
    left: 44px;
    bottom: 62px;
    display: flex;
    align-items: center;
    gap: 18px;
    color: var(--yellow);
    font-size: 64px;
    line-height: 1;
  }
  .signature__mark {
    width: 40px;
    height: 40px;
    background: var(--yellow);
  }
</style>
</head>
<body>
  <main class="card">
    <div class="card__field"></div>
    <div class="card__band"></div>

    <div class="mascot" role="img" aria-label="Illustration d'un bûcheron en chemise à carreaux rouge et jean, tenant un plateau de bûches"></div>

    <div class="pitch">
      <p>Livraison gratuite de bois de chauffage à Lyon et sa région</p>
      <p>Bûches, granulés, briquettes</p>
      <span class="pitch__gap"></span>
      <p>Commandez sur www.tafourmiliere.fr ou au 04 72 10 20 30</p>
      <span class="pitch__gap"></span>
      <p>Qualité supérieure, origine régionale certifiée, livraison en 48h</p>
    </div>

    <div class="signature">
      <span class="signature__mark"></span>
      <span class="signature__name">Ta Fourmilière</span>
    </div>
  </main>
</body>
</html>
```